Flyer for a marketing

We are a holistic mental health facility in need of a flyer to help promote our services and encourage more people to seek care. See the attachment to tell you more. We prefer warm green colors or rich blue. Thank you.

```html
<!DOCTYPE html>
<html lang="en">
<head>
<meta charset="utf-8">
<title>Evergreen Mind Health and Wellness – Flyer</title>
<link href="https://fonts.googleapis.com/css2?family=Merriweather:wght@700;900&family=Gelasio:wght@400;700&family=Montserrat:wght@300;400;600;700&family=Jost:wght@400&display=swap" rel="stylesheet">
<style>
:root{
  --backdrop:#5f6061;
  --paper:#ffffff;
  --green-dark:#2f7a3c;
  --green-mid:#3b8a3f;
  --green-band:#5fab5a;
  --ink:#2e2e2e;
  --grey-text:#5a5a5a;
}
*{margin:0;padding:0;box-sizing:border-box}
html,body{width:1031px;height:1200px;overflow:hidden;background:var(--backdrop)}
.flyer{position:absolute;left:115px;top:104px;width:796px;height:1031px;background:var(--paper);overflow:hidden}
.hero-photo{position:absolute;left:0;top:0;width:796px;height:470px;
  background:linear-gradient(180deg,rgba(255,255,255,0) 55%,#fff 100%),
  linear-gradient(100deg,#d9d6cf 0%,#b9a792 25%,#cfc6b8 50%,#c4ab90 75%,#e2d6c6 100%)}
.headline{position:absolute;left:0;width:100%;top:332px;text-align:center;font-family:'Merriweather',serif;font-weight:900;font-size:40px;line-height:47px;color:var(--ink)}
.tagline{position:absolute;left:0;width:100%;top:432px;text-align:center;font-family:'Gelasio',serif;font-size:20px;color:var(--ink)}
.banner{position:absolute;left:98px;top:488px;width:616px;height:41px}
.banner svg{position:absolute;inset:0}
.banner span{position:relative;display:block;text-align:center;line-height:41px;font-family:'Montserrat',sans-serif;font-weight:600;font-size:22px;color:#fff}
.prompt{position:absolute;left:0;width:100%;top:538px;text-align:center;font-family:'Montserrat',sans-serif;font-weight:300;font-size:22px;color:var(--grey-text)}
.cta{position:absolute;left:0;width:100%;top:565px;text-align:center;font-family:'Montserrat',sans-serif;font-weight:700;font-size:25px;color:var(--green-mid)}
.feature-band{position:absolute;left:0;top:673px;width:796px;height:185px;background:var(--green-band);border-top:3px solid var(--green-dark)}
.divider{position:absolute;top:686px;width:1px;height:155px;background:var(--green-dark)}
.feature-badge{position:absolute;top:619px;width:92px;height:106px}
.feature-text{position:absolute;top:728px;width:140px;text-align:center;font-family:'Montserrat',sans-serif;font-size:13px;line-height:17px;color:#fff;font-weight:400}
.feature-text b{font-weight:700}
.brand-block{position:absolute;left:40px;top:886px;width:260px;height:112px}
.brand-mark{position:absolute;left:14px;top:36px;width:52px;height:52px;border-radius:50%;background:var(--green-dark)}
.brand-rule{position:absolute;left:121px;top:0;width:2px;height:112px;background:var(--green-dark)}
.brand-name{position:absolute;left:145px;top:14px;font-family:'Gelasio',serif;font-weight:700;font-size:17px;line-height:19.5px;color:var(--green-dark)}
.contact{position:absolute;left:326px;top:884px}
.contact h2{font-family:'Montserrat',sans-serif;font-weight:700;font-size:17px;color:var(--green-mid);margin-bottom:8px}
.contact ul{list-style:none;font-family:'Jost',sans-serif;font-size:13px;color:var(--ink)}
.contact li{display:flex;align-items:center;height:20.5px;gap:5px}
.contact svg{width:11px;height:11px;flex:none}
</style>
</head>
<body>
<main class="flyer">
  <div class="hero-photo" role="img" aria-label="Photo of a smiling group of young friends outdoors in warm sunlight"></div>
  <h1 class="headline">Evergreen Mind Health<br>and Wellness</h1>
  <p class="tagline">where deserving patients meet compassionate providers.</p>

  <div class="banner">
    <svg viewBox="0 0 616 41" preserveAspectRatio="none"><polygon points="18,0 598,0 616,20.5 598,41 18,41 0,20.5" fill="var(--green-dark)"/></svg>
    <span>We are accepting new patients, no waiting list</span>
  </div>
  <p class="prompt">Your mental health matters, so make it a priority and</p>
  <p class="cta">call us today for an appointment</p>

  <div class="feature-band"></div>
  <div class="divider" style="left:164px"></div>
  <div class="divider" style="left:318px"></div>
  <div class="divider" style="left:487px"></div>
  <div class="divider" style="left:630px"></div>

  <!-- feature badges -->
  <svg class="feature-badge" style="left:46px" viewBox="0 0 92 106"><path d="M46 0 L92 46 L46 92 L0 46Z" fill="var(--green-dark)"/><path d="M46 92 L43 104 L49 104Z" fill="var(--green-dark)"/>
    <g fill="none" stroke="#fff" stroke-width="1.6"><rect x="32" y="32" width="28" height="30"/><rect x="40" y="26" width="12" height="10"/><path d="M46 28v6M43 31h6"/><path d="M36 40h4M36 46h4M52 40h4M52 46h4M28 62h36"/></g></svg>
  <svg class="feature-badge" style="left:196px" viewBox="0 0 92 106"><path d="M46 0 L92 46 L46 92 L0 46Z" fill="var(--green-dark)"/><path d="M46 92 L43 104 L49 104Z" fill="var(--green-dark)"/>
    <g fill="none" stroke="#fff" stroke-width="1.6"><path d="M46 42c-8-6-10-12-5-15 3-2 5 0 5 2 0-2 2-4 5-2 5 3 3 9-5 15z"/><path d="M30 36c0 10 6 16 12 20v6M62 36c0 10-6 16-12 20v6"/></g></svg>
  <svg class="feature-badge" style="left:364px" viewBox="0 0 92 106"><path d="M46 0 L92 46 L46 92 L0 46Z" fill="var(--green-dark)"/><path d="M46 92 L43 104 L49 104Z" fill="var(--green-dark)"/>
    <g fill="none" stroke="#fff" stroke-width="1.6"><rect x="26" y="30" width="16" height="22"/><path d="M29 36l2 2 3-3M29 44l2 2 3-3"/><circle cx="52" cy="38" r="9"/><path d="M58 45l6 7M40 58h22"/></g></svg>
  <svg class="feature-badge" style="left:514px" viewBox="0 0 92 106"><path d="M46 0 L92 46 L46 92 L0 46Z" fill="var(--green-dark)"/><path d="M46 92 L43 104 L49 104Z" fill="var(--green-dark)"/>
    <g fill="none" stroke="#fff" stroke-width="1.6"><rect x="28" y="40" width="10" height="22" rx="2"/><rect x="41" y="28" width="10" height="34" rx="2"/><rect x="54" y="40" width="10" height="22" rx="2"/></g></svg>
  <svg class="feature-badge" style="left:655px" viewBox="0 0 92 106"><path d="M46 0 L92 46 L46 92 L0 46Z" fill="var(--green-dark)"/><path d="M46 92 L43 104 L49 104Z" fill="var(--green-dark)"/>
    <g fill="none" stroke="#fff" stroke-width="1.6"><rect x="30" y="28" width="28" height="34" rx="3"/><rect x="38" y="25" width="12" height="6"/><path d="M36 38h6M39 35v6M46 38h8M36 46h18M36 52h12"/><path d="M56 50l6 2v5c0 3-3 5-6 6-3-1-6-3-6-6v-5z"/></g></svg>

  <p class="feature-text" style="left:22px">We are an<br><b>integrative holistic psychiatric center</b></p>
  <p class="feature-text" style="left:172px">Our mission<br>is to provide<br><b>compassionate quality<br>care</b></p>
  <p class="feature-text" style="left:335px;width:142px">We provide<br><b>psychiatric services including medication management and psychotherapy</b></p>
  <p class="feature-text" style="left:490px">We<br><b>listen, care,</b><br>and <b>empower you<br>to live better.</b></p>
  <p class="feature-text" style="left:638px">We accept<br><b>major<br>insurances</b></p>

  <div class="brand-block">
    <div class="brand-mark"></div>
    <div class="brand-rule"></div>
    <p class="brand-name">Evergreen<br>Mind<br>Health<br>and<br>Wellness</p>
  </div>

  <section class="contact">
    <h2>Evergreen Mind Health and Wellness, APNC</h2>
    <ul>
      <li><svg viewBox="0 0 12 12"><path d="M11 1L1 5.5l4.5 1.2L6.8 11z" fill="var(--green-dark)"/></svg>4180 Meadowbrook Road, Suite 310 Fairhaven, CA 90210</li>
      <li><svg viewBox="0 0 12 12"><path d="M1 5c0-2 2-3 5-3s5 1 5 3H8V4H4v1zM2 6h8l1 5H1z" fill="var(--green-dark)"/></svg>(555) 014-2287 &nbsp;&nbsp;<svg viewBox="0 0 12 12"><rect x="1" y="4" width="10" height="7" fill="var(--green-dark)"/><rect x="3" y="1" width="6" height="3" fill="none" stroke="var(--green-dark)"/></svg>(555) 017-9043</li>
      <li><svg viewBox="0 0 12 12"><rect x="0.5" y="2.5" width="11" height="7" fill="var(--green-dark)"/><path d="M1 3l5 4 5-4" stroke="#fff" fill="none"/></svg>hello@evergreenmindhealth.com</li>
      <li><svg viewBox="0 0 12 12"><g fill="none" stroke="var(--green-dark)"><circle cx="6" cy="6" r="5"/><ellipse cx="6" cy="6" rx="2" ry="5"/><path d="M1 6h10"/></g></svg>www.evergreenmindhealth.com</li>
    </ul>
  </section>
</main>
</body>
</html>
```